Small Catering Menu

I am looking to make a small menu for catering for my company. I am thinking of a small A5 size booklet which will also have some pictures and the cover needs to be attractive.
Likely to be 8-12 pages depending upon your design (could be less or more). I need 2-3 pages as proposal concept (Cover, inside first page and one menu page) and if we like it we will make the project guaranteed before finishing the rest of the project to add security for the designer.
Pictures will be provided to the designer whose concept is the best as they are too heavy. But use generic photos for now (rather large ones) if possible.
Logo is available and so is the inside text as well as some other tidbits.
I will provide the fonts too to ensure it maintains the corporate integrity that we are following.
Catering

```html
<!DOCTYPE html>
<html lang="en">
<head>
<meta charset="utf-8">
<title>Kids Catering Menu</title>
<link href="https://fonts.googleapis.com/css2?family=Source+Sans+3:wght@300;400&display=swap" rel="stylesheet">
<style>
  :root {
    --magenta: #e6037f;
    --raspberry: #e2135f;
    --ink: #2a0f1e;
    --sun: #fdbf12;
    --teal: #0f8f8b;
  }
  html, body {
    margin: 0;
    padding: 0;
    width: 1200px;
    height: 846px;
    overflow: hidden;
    background: #ffffff;
  }
  .menu-page {
    position: relative;
    width: 1200px;
    height: 846px;
    font-family: "Source Sans 3", "Source Sans Pro", sans-serif;
    font-weight: 300;
    color: var(--ink);
  }
  .hero-photo {
    position: absolute;
    left: 0; top: 0;
    width: 1200px; height: 346px;
    background:
      radial-gradient(ellipse 360px 200px at 560px 170px, #f4e9a6 0%, #efe08a 55%, rgba(239,224,138,0) 100%),
      radial-gradient(ellipse 260px 180px at 1040px 150px, #f07a2a 0%, rgba(240,122,42,0) 100%),
      linear-gradient(90deg, #6fbf3a 0%, #2aa3a8 22%, #1f8f9a 60%, #2c8a94 100%);
  }
  .menu-panel {
    position: absolute;
    left: 0; top: 346px;
    width: 692px; height: 500px;
  }
  .menu-panel svg {
    position: absolute;
    inset: 0;
  }
  .menu-list {
    position: absolute;
    left: 92px; top: 58px;
    width: 560px;
    margin: 0;
    padding: 0;
    list-style: none;
  }
  .menu-item { margin: 0 0 22px; }
  .menu-item + .menu-item { margin-top: 0; }
  .dish-name {
    display: block;
    font-size: 29px;
    line-height: 32px;
    font-weight: 300;
  }
  .dish-extras {
    display: block;
    font-size: 19px;
    line-height: 24px;
    font-weight: 300;
    margin-top: 4px;
  }
  .tile {
    position: absolute;
    width: 254px;
  }
  .tile--cake {
    left: 692px; top: 346px; height: 254px;
    background: linear-gradient(160deg, #b592d6 0%, #c9a7e0 40%, #f3a23a 70%, #fbe7d0 100%);
  }
  .tile--sun {
    left: 946px; top: 346px; height: 252px;
    background: var(--sun);
  }
  .tile--teal {
    left: 692px; top: 600px; height: 246px;
    background: var(--teal);
  }
  .tile--drink {
    left: 946px; top: 598px; height: 248px;
    background: radial-gradient(ellipse 120px 160px at 50% 60%, #5e7a6a 0%, #1f2a24 60%, #0b0f0c 100%);
  }
</style>
</head>
<body>
<main class="menu-page">
  <div class="hero-photo" role="img" aria-label="Photo of a bunny-face cheese sandwich with radish eyes and chive whiskers on a blue plate with an orange fork"></div>

  <section class="menu-panel">
    <svg width="692" height="500" viewBox="0 0 692 500" aria-hidden="true">
      <rect width="692" height="500" fill="var(--raspberry)"/>
      <polygon points="0,0 530,0 0,500" fill="var(--magenta)"/>
    </svg>
    <ul class="menu-list">
      <li class="menu-item">
        <span class="dish-name">Chicken Popcorn with Sweet Honey Mustard Sauce,</span>
        <span class="dish-extras">together with regular fries and orange juice “Fresh Box” (Including activity books)</span>
      </li>
      <li class="menu-item">
        <span class="dish-name">Beef Meat Balls,</span>
        <span class="dish-extras">together with regular fries and orange juice “Fresh Box” (Including activity books)</span>
      </li>
      <li class="menu-item">
        <span class="dish-name">Chicken Lollipop ,</span>
        <span class="dish-extras">together with regular fries and orange juice “Fresh Box” (Including activity books)</span>
      </li>
    </ul>
  </section>

  <div class="tile tile--cake" role="img" aria-label="Photo of a birthday jelly cake with fruit and lit candles at a party table"></div>
  <div class="tile tile--sun"></div>
  <div class="tile tile--teal"></div>
  <div class="tile tile--drink" role="img" aria-label="Photo of a fruit drink splashing in a glass with strawberries, lime and coconut on ice"></div>
</main>
</body>
</html>
```